Concrete Finishing business needs new business card and a logo design

We are a family owned and operated, concrete finishing business. 2020 marks our 33 rd year in business. We operate under Harold M. Ferrick and Sons Concrete Contractors Ltd. Harold M was my father and founder of the company. We usually shorten the name and use H M Ferrick & Sons Ltd. Most people in the Concrete Finishing industry tend to know us by our last name 'Ferrick' . in honour of our father, we would still like to have his name on the cards and logo but are open to shortening it to H.M (maybe in a small font with the W on top of the J ) and focusing more on the "Ferrick & Sons."....Or maybe something with just the initials HMF...or if you could use the "J" and somehow incorporate an artistic drawing/shape of a 'power trowel' (what we use apply a smooth finish to the concrete with) but still visually see that its a J, would be cool. Would like to see designs using Black with silver or grey lettering but are open to other ideas. Seen a business card online with the front of the business card looking like concrete and with just the word CONCRETE on it... On the back was the company name , address and contact info of the company....looked really good! i clicked doubled sided in case of something like that but we are open to just single sided as well. After viewing some of the designs, maybe a pop of colour would be nice ... open to any ideas and colours.😊

Target Market(s)

Construction

```html
<!DOCTYPE html>
<html lang="en">
<head>
<meta charset="utf-8">
<title>H.M. Ferrick &amp; Sons – Business Card</title>
<link rel="stylesheet" href="https://fonts.googleapis.com/css2?family=Raleway:wght@400;500;600;700;800&display=swap">
<style>
  :root {
    --bg: #161616;
    --card-black: #0b0b0b;
    --silver: #8c8c8c;
    --light: #e6e6e6;
    --white: #ffffff;
    --line: #6a6a6a;
    --concrete-1: #9a9c9d;
    --concrete-2: #7d7f80;
    --concrete-3: #6a6c6d;
  }
  html, body {
    margin: 0;
    padding: 0;
    width: 1200px;
    height: 900px;
    overflow: hidden;
    background: var(--bg);
    font-family: "Raleway", sans-serif;
  }
  .canvas {
    position: relative;
    width: 1200px;
    height: 900px;
    background: radial-gradient(ellipse at 40% 35%, #242424 0%, var(--bg) 70%);
  }

  /* Card back: contact side */
  .card-info {
    position: absolute;
    left: 70px;
    top: 120px;
    width: 520px;
    height: 310px;
    border-radius: 22px;
    background: var(--card-black);
    box-shadow: 0 0 0 1px #222;
    color: var(--light);
  }
  .card-info .rule-left {
    position: absolute;
    left: 34px;
    top: 40px;
    width: 1px;
    height: 170px;
    background: var(--line);
  }
  .brand {
    position: absolute;
    left: 60px;
    top: 56px;
    width: 190px;
  }
  .brand-mark {
    display: flex;
    align-items: center;
    gap: 12px;
  }
  .brand-initials {
    font-weight: 800;
    font-size: 52px;
    letter-spacing: 2px;
    color: var(--silver);
    line-height: 1;
  }
  .brand-square {
    width: 30px;
    height: 30px;
    border: 3px solid var(--white);
    box-sizing: border-box;
  }
  .brand-name {
    margin-top: 12px;
    font-size: 14px;
    font-weight: 500;
    letter-spacing: 0.5px;
    color: var(--light);
  }
  .contact {
    position: absolute;
    left: 270px;
    top: 50px;
    font-size: 16px;
    font-weight: 600;
    line-height: 1.5;
    color: var(--light);
  }
  .contact .address { margin-bottom: 12px; }
  .contact-row {
    display: flex;
    align-items: center;
    gap: 10px;
  }
  .contact-row svg { width: 14px; height: 14px; fill: var(--silver); flex: none; }
  .tagline {
    position: absolute;
    left: 34px;
    right: 34px;
    bottom: 44px;
    display: flex;
    align-items: center;
    gap: 14px;
    font-size: 13px;
    font-weight: 500;
    letter-spacing: 0.6px;
    color: var(--silver);
    white-space: nowrap;
  }
  .tagline::after {
    content: "";
    flex: 1;
    height: 1px;
    background: var(--line);
  }

  /* Card front: concrete side */
  .card-concrete {
    position: absolute;
    left: 630px;
    top: 120px;
    width: 500px;
    height: 310px;
    border-radius: 22px;
    background: linear-gradient(160deg, var(--concrete-1) 0%, var(--concrete-2) 55%, var(--concrete-3) 100%);
    display: flex;
    align-items: center;
    justify-content: center;
  }
  .concrete-frame {
    padding: 10px 22px;
    border: 3px solid #5f6162;
    box-shadow: 1px 1px 0 rgba(255,255,255,0.25), inset 1px 1px 0 rgba(255,255,255,0.2);
  }
  .concrete-word {
    font-weight: 700;
    font-size: 46px;
    letter-spacing: 6px;
    color: #767879;
    text-shadow: 1px 1px 0 rgba(255,255,255,0.3), -1px -1px 0 rgba(0,0,0,0.3);
  }

  /* Logo lockup */
  .logo-lockup {
    position: absolute;
    right: 60px;
    bottom: 70px;
    width: 420px;
    text-align: center;
  }
  .logo-lockup .lockup-mark {
    display: flex;
    align-items: center;
    justify-content: center;
    gap: 22px;
  }
  .logo-lockup .lockup-initials {
    font-weight: 800;
    font-size: 110px;
    letter-spacing: 6px;
    color: var(--silver);
    line-height: 1;
  }
  .logo-lockup .lockup-square {
    width: 64px;
    height: 64px;
    border: 5px solid var(--white);
    box-sizing: border-box;
  }
  .logo-lockup .lockup-name {
    margin-top: 18px;
    font-size: 32px;
    font-weight: 400;
    letter-spacing: 0.5px;
    color: var(--white);
  }
</style>
</head>
<body>
<main class="canvas">

  <section class="card-info" aria-label="Business card, contact side">
    <div class="rule-left"></div>
    <div class="brand">
      <div class="brand-mark">
        <span class="brand-initials">HMF</span>
        <span class="brand-square"></span>
      </div>
      <div class="brand-name">H.M.FERRICK &amp; SONS</div>
    </div>
    <div class="contact">
      <div class="address">P.O.Box 47, Site 9, RR#2<br>Harbour Point, NL, A0K 3B0</div>
      <div class="contact-row">
        <svg viewBox="0 0 24 24" aria-hidden="true"><path d="M6.6 10.8a15 15 0 0 0 6.6 6.6l2.2-2.2c.3-.3.7-.4 1-.2 1.1.4 2.3.6 3.6.6.6 0 1 .4 1 1V20c0 .6-.4 1-1 1A17 17 0 0 1 3 4c0-.6.4-1 1-1h3.5c.6 0 1 .4 1 1 0 1.3.2 2.5.6 3.6.1.3 0 .7-.2 1z"/></svg>
        <span>(555) 214-6081</span>
      </div>
      <div class="contact-row">
        <svg viewBox="0 0 24 24" aria-hidden="true"><path d="M4 3h16v18H4zM6 5v4h12V5zm0 6v2h3v-2zm5 0v2h2v-2zm4 0v2h3v-2zM6 15v2h3v-2zm5 0v2h2v-2zm4 0v4h3v-4z"/></svg>
        <span>(555) 214-5527</span>
      </div>
      <div class="contact-row">
        <svg viewBox="0 0 24 24" aria-hidden="true"><path d="M7 2h10a2 2 0 0 1 2 2v16a2 2 0 0 1-2 2H7a2 2 0 0 1-2-2V4a2 2 0 0 1 2-2zm0 3v13h10V5z"/></svg>
        <span>(555) 214-9046</span>
      </div>
      <div class="contact-row">
        <svg viewBox="0 0 24 24" aria-hidden="true"><path d="M2 5h20v14H2zm2 2v.5l8 5 8-5V7zm0 2.8V17h16V9.8l-8 5z"/></svg>
        <span>hm.ferrick@example.com</span>
      </div>
    </div>
    <div class="tagline">SPECIALIZING IN CONCRETE FLOOR FINISHING</div>
  </section>

  <section class="card-concrete" role="img" aria-label="Business card front with a cast concrete texture and the word CONCRETE pressed into it">
    <div class="concrete-frame">
      <span class="concrete-word">CONCRETE</span>
    </div>
  </section>

  <section class="logo-lockup" aria-label="Company name lockup">
    <div class="lockup-mark">
      <span class="lockup-initials">HMF</span>
      <span class="lockup-square"></span>
    </div>
    <div class="lockup-name">H.M.FERRICK &amp; SONS</div>
  </section>

</main>
</body>
</html>
```